Brewvine web designing - Brewvine

We need a business-charity purpose online shop selling premium herbal teas with a tagline "Healthy with a heart" where all the raw materials are being purchased from Indonesian local farmers in order to give them sustainable employment. Every 20% from the total amount of the customer's purchase from our website always goes back to their communities to help build better sanitation, education or whatever they need. We need page to blog too and another page for customers to interact and share their thought. we expect an eye catching simple earthy (maybe a bit rustic) design with some brush lettering font in some parts. Thank you.

Target Market(s)

-Tea Lovers
-Anyone with body weight issues or any health issues in general

Industry/Entity Type

Home Health Care

Number of Pages Required

5+ page

Font styles to use
Other font styles liked:
• brush lettering font in some parts

Requirements
Must have
• - Brush lettering font
• -Simple, a bit rustic design with some nice watercolor touch
• -Blogging Page
• -catchy yet fancy and elegant E-commerce page
Nice to have
• Well, I will let the designers use their skills and imaginations to the fullest.

```html
<!DOCTYPE html>
<html lang="en">
<head>
<meta charset="utf-8">
<title>Brewvine – Healthy with a heart</title>
<link rel="stylesheet" href="https://fonts.googleapis.com/css2?family=Baumans&family=Raleway:wght@400;500;600;700&family=Open+Sans:wght@400;600&display=swap">
<style>
:root{
  --leaf:#76a912;
  --olive:#9b8a3f;
  --sage:#6f8a4f;
  --ink:#333326;
  --text:#4a4a4a;
  --blue:#1f4d9a;
  --tile:#eef0f4;
  --night:#1f1f1d;
  --white:#ffffff;
}
*{box-sizing:border-box;margin:0;padding:0}
html,body{width:1200px;height:2731px;overflow:hidden}
body{position:relative;background:var(--white);font-family:"Raleway",sans-serif;color:var(--text)}
.abs{position:absolute}
.display{font-family:"Baumans",sans-serif;font-weight:400}

/* top bar */
.topbar{left:0;top:0;width:1200px;height:19px;background:var(--leaf);color:var(--white);font-size:8px}
.topbar .social{left:250px;top:5px;display:flex;gap:10px}
.topbar .social span{width:8px;height:8px;border-radius:50%;background:rgba(255,255,255,.85)}
.topbar .promo{left:0;width:1200px;top:5px;text-align:center}
.topbar .cart{left:832px;top:4px;display:flex;gap:14px;align-items:center;font-weight:600}

/* header */
.header{left:0;top:19px;width:1200px;height:69px;background:var(--white)}
.logo{left:250px;top:29px;display:flex;align-items:center;gap:6px;font-size:13px;font-weight:700;color:var(--ink)}
.logo i{width:10px;height:10px;border-radius:50%;background:var(--leaf)}
.nav{left:443px;top:31px;display:flex;gap:18px;font-size:12px;color:var(--ink)}
.btn{display:flex;align-items:center;justify-content:center;background:var(--olive);color:var(--white);border-radius:20px;font-size:13px}
.header .btn{left:836px;top:19px;width:114px;height:31px;font-size:14px}

/* hero */
.hero{left:0;top:88px;width:1200px;height:400px;background:linear-gradient(100deg,#e3ecc8 0%,#f6f8ee 35%,#fbfcf7 60%,#e9f0cf 100%)}
.hero-photo{left:565px;top:49px;width:418px;height:291px;border-radius:46% 46% 40% 40%;background:radial-gradient(ellipse at 50% 55%,#d8b43a 0%,#e8d89a 40%,rgba(240,242,230,0) 72%)}
.hero h1{left:250px;top:130px;font-size:30px;color:var(--leaf)}
.hero p{left:250px;top:178px;width:305px;font-size:9px;line-height:13px;color:#3b3b3b}
.hero .btn{left:250px;top:240px;width:118px;height:31px}

/* about */
.about{left:0;top:488px;width:1200px;height:286px;background:linear-gradient(#fafafa,#f1f1f1)}
.about h2{left:250px;top:56px;font-size:34px;color:var(--leaf)}
.about p{left:250px;top:112px;width:425px;font-size:9px;line-height:13px}
.about .more{left:250px;top:189px;font-size:11px;font-weight:600;color:var(--ink);display:flex;align-items:center;gap:5px}
.about .more i{width:10px;height:10px;border-radius:50%;background:var(--olive)}
.about-photo{left:674px;top:40px;width:273px;height:191px;border-radius:50%;background:radial-gradient(ellipse at 55% 45%,#c9c24a 0%,#e2e3b8 45%,rgba(241,241,241,0) 72%)}

/* steps */
.steps{left:0;top:774px;width:1200px;height:432px}
.steps-photo{left:0;top:0;width:1200px;height:432px;background:linear-gradient(180deg,#dca068 0%,#eebd86 40%,#e6ab6e 72%,#a45d2c 86%,#6e3a1c 100%)}
.steps h2{left:0;width:1200px;top:26px;text-align:center;font-size:35px;color:var(--ink);padding-right:60px}
.step{top:93px;width:190px;text-align:center}
.step .ring{margin:0 auto;width:114px;height:114px;border-radius:50%;background:var(--white);display:flex;align-items:center;justify-content:center}
.step .ring span{width:100px;height:100px;border-radius:50%;background:var(--sage);display:flex;align-items:center;justify-content:center}
.step h3{margin-top:12px;font-size:13px;font-weight:500;color:#222}
.step p{margin-top:8px;font-size:8.5px;line-height:14px;color:#3a2a1a}

/* shop */
.section-title{left:0;width:1200px;text-align:center;font-size:33px;color:var(--ink)}
.card{top:1309px;width:160px;height:190px;border:1px solid #dcdcdc;background:var(--white)}
.card .photo{position:absolute;left:4px;top:4px;width:150px;height:134px;background:radial-gradient(ellipse at 45% 55%,#c7c54a 0%,#e6ead0 45%,#fbfbf8 72%)}
.card .acts{position:absolute;right:8px;top:30px;display:flex;flex-direction:column;gap:8px}
.card .acts span{width:20px;height:20px;border-radius:50%;background:#8c8c84;display:flex;align-items:center;justify-content:center}
.card .tag{position:absolute;left:0;top:141px;width:120px;height:21px;background:var(--sage);clip-path:polygon(0 0,100% 0,88% 100%,0 100%);color:var(--white);font-size:12px;line-height:21px;padding-left:7px}
.card .price{position:absolute;left:7px;top:168px;font-size:12px;color:#333}
.dots{left:0;width:1200px;top:1522px;text-align:center;font-size:12px;letter-spacing:3px;color:#555}
.rule{left:0;top:1573px;width:1200px;height:1px;background:#9a9a9a}
.shop-btn{left:519px;top:1553px;width:160px;height:39px;font-size:13px}

/* blog */
.blog{left:250px;top:1694px;width:700px;height:355px;display:grid;grid-template-columns:repeat(3,1fr);grid-template-rows:repeat(2,1fr)}
.blog .img{width:100%;height:100%}
.blog .post{background:var(--tile);padding:12px 6px 0 6px;position:relative}
.post h4{font-size:13px;font-weight:700;color:var(--blue)}
.post time{display:block;margin-top:9px;font-size:8px;color:#555}
.post p{margin-top:9px;font-size:8.5px;line-height:13px;color:#333}
.post a{display:block;margin-top:8px;font-size:9px;font-weight:700;color:var(--blue);text-decoration:none}
.post .corner{position:absolute;right:0;bottom:0;width:0;height:0;border-left:9px solid transparent;border-bottom:9px solid var(--blue)}

/* testimonial */
.reviews{left:0;top:2094px;width:1200px;height:343px;background:radial-gradient(ellipse at 50% 60%,#5a4c2c 0%,#2e2a1e 45%,#141410 100%)}
.reviews h2{left:0;width:1200px;top:36px;text-align:center;font-size:33px;color:var(--white)}
.avatar{left:565px;top:118px;width:70px;height:70px;border-radius:50%;background:#c9a27a;border:3px solid var(--white)}
.reviews .name{left:0;width:1200px;top:201px;text-align:center;font-size:16px;color:var(--white)}
.reviews p{left:260px;width:680px;top:236px;text-align:center;font-size:9px;line-height:14px;color:#eee}
.reviews time{left:0;width:1200px;top:293px;text-align:center;font-size:9px;color:#eee}

/* newsletter */
.newsletter{left:0;top:2437px;width:1200px;height:82px;background:var(--white)}
.newsletter h2{left:250px;top:23px;font-size:28px;color:var(--sage)}
.newsletter .field{left:581px;top:25px;width:233px;height:31px;border:1px solid #cfcfcf;border-radius:16px;background:#f3f3f3;font-size:9px;color:#aaa;text-align:center;line-height:29px}
.newsletter .btn{left:832px;top:25px;width:115px;height:31px;font-size:14px}

/* footer */
.footer{left:0;top:2519px;width:1200px;height:212px;background:var(--night);font-family:"Open Sans",sans-serif}
.fcol{top:28px}
.fcol h5{font-size:13px;font-weight:600;color:#d4d4d4;margin-bottom:7px}
.fcol li{list-style:none;font-size:10px;line-height:22px;color:#9e9e9e}
.footer .line{left:0;top:178px;width:1200px;height:1px;background:#3a3a3a}
.footer .copy{left:250px;top:188px;font-size:8px;color:#777}
</style>
</head>
<body>

<div class="abs topbar">
  <div class="abs social"><span></span><span></span><span></span><span></span><span></span><span></span></div>
  <div class="abs promo">20% from the total amount of the customer's purchase</div>
  <div class="abs cart">
    <span style="display:flex;align-items:center;gap:4px">
      <svg width="10" height="9" viewBox="0 0 10 9"><path d="M0 1h2l1.3 5h5l1-3.5H3" fill="none" stroke="#fff" stroke-width="1.1"/><circle cx="4" cy="8" r=".9" fill="#fff"/><circle cx="8" cy="8" r=".9" fill="#fff"/></svg>Add to Cart</span>
    <span>0 Items</span>
  </div>
</div>

<div class="abs header">
  <div class="abs logo"><span>Brewvine</span><i></i></div>
  <nav class="abs nav"><span>Home</span><span>About Us</span><span>Product</span><span>Education</span><span>Blog</span><span>Contact Us</span></nav>
  <div class="abs btn">Started Now</div>
</div>

<section class="abs hero">
  <div class="abs hero-photo" role="img" aria-label="Glass teapot with blooming tea and a cup of golden herbal tea among green leaves"></div>
  <h1 class="abs display">Healthy with a heart</h1>
  <p class="abs">Lorem Ipsum is simply dummy text of the printing and typesetting industry. Lorem Ipsum has been the industry's standard dummy text ever since the 1500s, when an unknown</p>
  <div class="abs btn">Get Started</div>
</section>

<section class="abs about">
  <h2 class="abs display">About us</h2>
  <p class="abs">Lorem Ipsum is simply dummy text of the printing and typesetting industry. Lorem Ipsum has been the industry's standard dummy text ever since the 1500s, when an unknown printer took a galley of type and scrambled it to make a type specimen book. It has survived not only five centuries, but also the leap into electronic typesetting, remaining essentially unchanged. It was popularised in the</p>
  <div class="abs more">Add Your Product Now <i></i></div>
  <div class="abs about-photo" role="img" aria-label="Glass cup of green herbal tea on a saucer with fresh leaves"></div>
</section>

<section class="abs steps">
  <div class="abs steps-photo" role="img" aria-label="Warm wooden table with lemon slices and a glass of amber tea in an ornate holder"></div>
  <h2 class="abs display">Three Easy Step to Sell Your Product</h2>
  <div class="abs step" style="left:240px">
    <div class="ring"><span><svg width="40" height="40" viewBox="0 0 40 40" fill="none" stroke="#fff" stroke-width="2"><circle cx="22" cy="13" r="6"/><path d="M12 32c0-7 4-11 10-11s10 4 10 11"/><circle cx="11" cy="27" r="4"/></svg></span></div>
    <h3>Create an Account</h3>
    <p>Lorem Ipsum is simply dummy text of the printing and typesetting industry. Lorem Ipsum has been the industry's standard dummy text ever</p>
  </div>
  <div class="abs step" style="left:457px">
    <div class="ring"><span><svg width="40" height="40" viewBox="0 0 40 40" fill="none" stroke="#fff" stroke-width="2"><circle cx="20" cy="20" r="16"/><path d="M20 12v16M12 20h16"/></svg></span></div>
    <h3>Add Product</h3>
    <p>Lorem Ipsum is simply dummy text of the printing and typesetting industry. Lorem Ipsum has been the industry's standard dummy text ever</p>
  </div>
  <div class="abs step" style="left:673px">
    <div class="ring"><span><svg width="40" height="40" viewBox="0 0 40 40" fill="none" stroke="#fff" stroke-width="2"><path d="M6 9h5l4 16h15l3-11H13"/><circle cx="17" cy="31" r="2"/><circle cx="28" cy="31" r="2"/></svg></span></div>
    <h3>Add Product</h3>
    <p>Lorem Ipsum is simply dummy text of the printing and typesetting industry. Lorem Ipsum has been the industry's standard dummy text ever</p>
  </div>
</section>

<h2 class="abs section-title display" style="top:1240px">Shop</h2>

<div class="abs card" style="left:250px">
  <div class="photo" role="img" aria-label="Cup of green herbal tea with leaves"></div>
  <div class="acts"><span><svg width="10" height="9" viewBox="0 0 10 9"><path d="M5 8.5 1 4.5a2.2 2.2 0 0 1 4-2.7 2.2 2.2 0 0 1 4 2.7z" fill="#fff"/></svg></span><span><svg width="10" height="7" viewBox="0 0 10 7"><ellipse cx="5" cy="3.5" rx="4.5" ry="3" fill="#fff"/><circle cx="5" cy="3.5" r="1.3" fill="#8c8c84"/></svg></span><span><svg width="9" height="9" viewBox="0 0 9 9"><path d="M1 3h7l-.7 6H1.7z" fill="#fff"/><path d="M3 3V2a1.5 1.5 0 0 1 3 0v1" stroke="#fff" fill="none"/></svg></span></div>
  <div class="tag">Herbal tea</div><div class="price">$ 30.00</div>
</div>
<div class="abs card" style="left:430px">
  <div class="photo" role="img" aria-label="Cup of green herbal tea with leaves"></div>
  <div class="acts"><span><svg width="10" height="9" viewBox="0 0 10 9"><path d="M5 8.5 1 4.5a2.2 2.2 0 0 1 4-2.7 2.2 2.2 0 0 1 4 2.7z" fill="#fff"/></svg></span><span><svg width="10" height="7" viewBox="0 0 10 7"><ellipse cx="5" cy="3.5" rx="4.5" ry="3" fill="#fff"/><circle cx="5" cy="3.5" r="1.3" fill="#8c8c84"/></svg></span><span><svg width="9" height="9" viewBox="0 0 9 9"><path d="M1 3h7l-.7 6H1.7z" fill="#fff"/><path d="M3 3V2a1.5 1.5 0 0 1 3 0v1" stroke="#fff" fill="none"/></svg></span></div>
  <div class="tag">Herbal tea</div><div class="price">$ 30.00</div>
</div>
<div class="abs card" style="left:610px">
  <div class="photo" role="img" aria-label="Cup of green herbal tea with leaves"></div>
  <div class="acts"><span><svg width="10" height="9" viewBox="0 0 10 9"><path d="M5 8.5 1 4.5a2.2 2.2 0 0 1 4-2.7 2.2 2.2 0 0 1 4 2.7z" fill="#fff"/></svg></span><span><svg width="10" height="7" viewBox="0 0 10 7"><ellipse cx="5" cy="3.5" rx="4.5" ry="3" fill="#fff"/><circle cx="5" cy="3.5" r="1.3" fill="#8c8c84"/></svg></span><span><svg width="9" height="9" viewBox="0 0 9 9"><path d="M1 3h7l-.7 6H1.7z" fill="#fff"/><path d="M3 3V2a1.5 1.5 0 0 1 3 0v1" stroke="#fff" fill="none"/></svg></span></div>
  <div class="tag">Herbal tea</div><div class="price">$ 30.00</div>
</div>
<div class="abs card" style="left:790px">
  <div class="photo" role="img" aria-label="Cup of green herbal tea with leaves"></div>
  <div class="acts"><span><svg width="10" height="9" viewBox="0 0 10 9"><path d="M5 8.5 1 4.5a2.2 2.2 0 0 1 4-2.7 2.2 2.2 0 0 1 4 2.7z" fill="#fff"/></svg></span><span><svg width="10" height="7" viewBox="0 0 10 7"><ellipse cx="5" cy="3.5" rx="4.5" ry="3" fill="#fff"/><circle cx="5" cy="3.5" r="1.3" fill="#8c8c84"/></svg></span><span><svg width="9" height="9" viewBox="0 0 9 9"><path d="M1 3h7l-.7 6H1.7z" fill="#fff"/><path d="M3 3V2a1.5 1.5 0 0 1 3 0v1" stroke="#fff" fill="none"/></svg></span></div>
  <div class="tag">Herbal tea</div><div class="price">$ 30.00</div>
</div>

<div class="abs dots">••••</div>
<div class="abs rule"></div>
<div class="abs btn shop-btn">View All Product</div>

<h2 class="abs section-title display" style="top:1628px">Our Blog</h2>
<div class="abs blog">
  <div class="img" role="img" aria-label="Glass teapots of amber tea on a green background" style="background:linear-gradient(160deg,#6d8f1c,#a8b83a 45%,#b8621c)"></div>
  <article class="post">
    <h4>Seal Herbal Tea</h4><time>31 March 2017</time>
    <p>Lorem Ipsum is simply dummy text of the printing and typesetting industry. Lorem Ipsum has been the industry's standard dummy text ever since the 1500s, when an unknown printer took a galley of type and scrambled it to make a type specimen book. It has survived</p>
    <a>Read More</a>
  </article>
  <div class="img" role="img" aria-label="Hands writing beside a laptop on a desk" style="background:linear-gradient(135deg,#5e6a78,#c9ced4 50%,#e7e8ea)"></div>
  <article class="post">
    <h4>Herbal Tea</h4><time>31 March 2017</time>
    <p>Lorem Ipsum is simply dummy text of the printing and typesetting industry. Lorem Ipsum has been the industry's standard dummy text ever since the 1500s, when an unknown printer took a galley of type and scrambled it to make a type specimen book. It has survived</p>
    <a>Read More</a><span class="corner"></span>
  </article>
  <div class="img" role="img" aria-label="Tea being poured into a glass cup" style="background:radial-gradient(ellipse at 50% 65%,#c07a22 0%,#e4c48a 40%,#f4f1e8 75%)"></div>
  <article class="post">
    <h4>Typesetting Industry</h4><time>31 March 2017</time>
    <p>Lorem Ipsum is simply dummy text of the printing and typesetting industry. Lorem Ipsum has been the industry's standard dummy text ever since the 1500s, when an unknown printer took a galley of type and scrambled it to make a type specimen book. It has survived</p>
    <a>Read More</a><span class="corner"></span>
  </article>
</div>

<section class="abs reviews" role="img" aria-label="Dark blurred photo of a glass tea cup behind the client quote">
  <h2 class="abs display">What Client says</h2>
  <div class="abs avatar" role="img" aria-label="Client portrait"></div>
  <div class="abs name">Lena Marsh</div>
  <p class="abs">Clara was extremely helpful during the entire process. Moving to another country is a very challenging ordeal and having someone like Clara on your side makes all the difference. She's continued to be incredibly helpful even after arriving, fielding every one of my questions and following up with helpful suggestions. She has been a critical part of the process!</p>
  <time class="abs">January 2, 2017</time>
</section>

<section class="abs newsletter">
  <h2 class="abs display">Sign up for Newsletter</h2>
  <div class="abs field">Enter Email</div>
  <div class="abs btn">Sign Up</div>
</section>

<footer class="abs footer">
  <div class="abs fcol" style="left:255px"><h5>News &amp; Media</h5><ul><li>Latest Stories</li><li>Press Releases</li><li>Media Inquiries</li><li>Media Partners</li><li>The News</li></ul></div>
  <div class="abs fcol" style="left:441px"><h5>Support</h5><ul><li>Latest Stories</li><li>Press Releases</li><li>Media Inquiries</li><li>Media Partners</li><li>The News</li></ul></div>
  <div class="abs fcol" style="left:615px"><h5>Event</h5><ul><li>Latest Stories</li><li>Press Releases</li><li>Media Inquiries</li><li>Media Partners</li><li>The News</li></ul></div>
  <div class="abs fcol" style="left:772px"><h5>News &amp; Media</h5><ul><li>Submit Your Story</li><li>Member Updates Archive</li><li>Contact</li><li>Login</li></ul></div>
  <div class="abs line"></div>
  <div class="abs copy">© brewvine-tea.com - 2017. All Rights Reserved. · Privacy Policy · Legal Usage Policy · Sitemap</div>
</footer>

</body>
</html>
```